Where's my Gym Buddy? looking to do two promotions as listed in project description

looking for two designs.

1: selfie frame design!! (wording) Frost Grind Carnival, my Summer fitness has started, Tag a friend who should be joining me. T.C Tag your posts to @brightloopsydney to win points for the competition. (Snow graphic) in a selfie frame design. this needs to be the same design but across different departments as seen at the top of the photo's I've attached EG: #brightloopfitness #brightloopindoor #brightloopswim #brightloopwyong

2: Selfie Frame Design!! (Wording) Where's my gym buddy?, Tag a friend who should be at the gym, T.C.Tag your posts to @brightloopsydney to win points for the competition. Spot the Pilot Feel Selfie frame design

Target Market(s)

Gym Members

Industry/Entity Type

Gym

Colors

Designer to choose colors to be used in the design.

Requirements
Must have
• quirky and funky design, must include wording listed, must be a selfie frame design
Should not have
• whilst we are a big corporate gym, we pride ourselves on having really funky advertisements, so please no boring business corporate typical designs

```html
<!DOCTYPE html>
<html lang="en">
<head>
<meta charset="utf-8">
<title>Where's my Gym Buddy? Selfie Frames</title>
<link rel="stylesheet" href="https://fonts.googleapis.com/css2?family=Caveat+Brush&family=Montserrat:wght@400;600;700&display=swap">
<style>
  :root {
    --page-bg: #e6e6e6;
    --frame-white: #ffffff;
    --header-blue: #1d5a8c;
    --winter-blue: #1ca4e6;
    --stripe-red: #d9120f;
    --photo-deep: #2a3560;
    --photo-mid: #5f8ea0;
    --photo-light: #c9dcc2;
    --nav-dark: #222326;
    --nav-cell: #2e2f33;
    --nav-active: #1d5a8c;
    --avatar: #1a1a1a;
    --text-dark: #2b2b2b;
    --meta-grey: #9a9a9a;
    --button-bg: #ececec;
    --button-text: #a0a0a0;
    --battery-green: #3cc43c;
  }
  * { margin: 0; padding: 0; box-sizing: border-box; }
  html, body {
    width: 1200px; height: 848px; overflow: hidden;
    background: var(--page-bg);
    font-family: "Montserrat", Arial, sans-serif;
  }
  .board {
    position: absolute; left: 0; top: 0;
    width: 1170px; height: 827px;
    transform: scale(1.0256); transform-origin: 0 0;
  }
  .selfie-frame {
    position: absolute; top: 100px;
    width: 439px; height: 566px;
    background: var(--frame-white);
  }
  .selfie-frame--winter { left: 131px; }
  .selfie-frame--buddy { left: 599px; }

  .side-band { position: absolute; top: 0; height: 566px; }
  .side-band--left { left: 0; width: 54px; }
  .side-band--right { right: 0; width: 56px; }
  .selfie-frame--winter .side-band { background: var(--winter-blue); }
  .selfie-frame--buddy .side-band {
    background: repeating-linear-gradient(to bottom,
      var(--stripe-red) 0 42px, var(--frame-white) 42px 60px);
  }

  .app-header {
    position: absolute; left: 64px; top: 10px;
    width: 308px; height: 62px;
    background: var(--header-blue);
    color: var(--frame-white);
  }
  .status-dots { position: absolute; left: 6px; top: 5px; }
  .battery { position: absolute; right: 6px; top: 5px; }
  .app-title {
    position: absolute; left: 0; right: 36px; top: 9px;
    text-align: center;
    font-family: "Caveat Brush", cursive;
    font-weight: 400; font-size: 27px; line-height: 28px;
    letter-spacing: 0.3px;
  }
  .selfie-frame--buddy .app-title { top: 18px; font-size: 28px; }
  .app-subtitle {
    position: absolute; left: 0; right: 36px; top: 39px;
    text-align: center;
    font-size: 9.5px; font-weight: 400; letter-spacing: 0.2px;
  }
  .inbox-icon { position: absolute; right: 10px; top: 30px; }

  .post-avatar {
    position: absolute; left: 72px; top: 80px;
    width: 31px; height: 31px; border-radius: 50%;
    background: var(--avatar);
  }
  .post-time { position: absolute; left: 321px; top: 88px; }

  .selfie-photo {
    position: absolute; left: 64px; top: 118px;
    width: 310px; height: 309px;
    background: radial-gradient(ellipse 60% 65% at 60% 62%,
      var(--photo-light) 0%, var(--photo-mid) 55%, var(--photo-deep) 100%);
  }

  .post-caption {
    position: absolute; left: 72px; top: 434px;
    font-size: 9.6px; line-height: 10.5px;
    color: var(--text-dark); text-transform: uppercase;
    letter-spacing: 0.1px;
  }
  .post-caption p { position: relative; padding-left: 14px; }
  .caption-icon { position: absolute; left: 0; top: 1px; }

  .post-actions {
    position: absolute; left: 72px; top: 482px; width: 290px; height: 22px;
  }
  .action-button {
    position: absolute; top: 0; height: 22px;
    background: var(--button-bg); color: var(--button-text);
    font-size: 13px; font-weight: 600;
    display: flex; align-items: center; gap: 5px; padding: 0 6px;
  }
  .action-button--like { left: 0; width: 59px; }
  .action-button--comment { left: 65px; width: 94px; }
  .action-button--more { left: 255px; width: 35px; justify-content: center; }

  .app-nav {
    position: absolute; left: 64px; top: 514px;
    width: 308px; height: 44px;
    display: flex; gap: 1px; background: var(--nav-dark);
  }
  .nav-item {
    flex: 1; display: flex; align-items: center; justify-content: center;
    background: var(--nav-cell);
  }
  .nav-item:first-child { background: var(--nav-dark); }
  .nav-item--active { background: var(--nav-active); }
</style>
</head>
<body>
<main class="board">

  <!-- Frost Grind Carnival frame -->
  <section class="selfie-frame selfie-frame--winter">
    <div class="side-band side-band--left" role="img" aria-label="White snowflake pattern on bright blue"></div>
    <div class="side-band side-band--right" role="img" aria-label="White snowflake pattern on bright blue"></div>

    <header class="app-header">
      <svg class="status-dots" width="26" height="6" viewBox="0 0 26 6"><circle cx="3" cy="3" r="2.5" fill="#fff"/><circle cx="9" cy="3" r="2.5" fill="#fff"/><circle cx="15" cy="3" r="2.5" fill="#fff"/><circle cx="21" cy="3" r="2.2" fill="none" stroke="#fff"/></svg>
      <svg class="battery" width="22" height="9" viewBox="0 0 22 9"><rect x="0.5" y="0.5" width="19" height="8" fill="none" stroke="#fff"/><rect x="2" y="2" width="12" height="5" fill="var(--battery-green)"/><rect x="20" y="3" width="2" height="3" fill="#fff"/></svg>
      <h1 class="app-title">Frost Grind Carnival</h1>
      <p class="app-subtitle">MY SUMMER FITNESS HAS STARTED</p>
      <svg class="inbox-icon" width="20" height="18" viewBox="0 0 20 18"><path d="M2 7 L5 1 H15 L18 7 V16 H2 Z M2 7 H7 V10 H13 V7 H18" fill="none" stroke="#fff" stroke-width="2" stroke-linejoin="round"/></svg>
    </header>

    <div class="post-avatar"></div>
    <svg class="post-time" width="10" height="10" viewBox="0 0 10 10"><circle cx="5" cy="5" r="4.5" fill="var(--meta-grey)"/><path d="M5 2.5 V5 H7" stroke="#fff" stroke-width="1" fill="none"/></svg>

    <div class="selfie-photo" role="img" aria-label="Open selfie window, soft blurred blue-green backdrop"></div>

    <div class="post-caption">
      <p><svg class="caption-icon" width="9" height="8" viewBox="0 0 9 8"><path d="M4.5 7.5 L0.8 3.8 A2 2 0 0 1 4.5 1.5 A2 2 0 0 1 8.2 3.8 Z" fill="#bbb"/></svg>Tag a friend who should be joining me.</p>
      <p><svg class="caption-icon" width="9" height="8" viewBox="0 0 9 8"><ellipse cx="4.5" cy="3.7" rx="4.2" ry="3.3" fill="#bbb"/></svg>T.C tag your posts to @brightloopsydney</p>
      <p>to win points for the competition.</p>
    </div>

    <div class="post-actions">
      <span class="action-button action-button--like"><svg width="13" height="12" viewBox="0 0 9 8"><path d="M4.5 7.5 L0.8 3.8 A2 2 0 0 1 4.5 1.5 A2 2 0 0 1 8.2 3.8 Z" fill="var(--button-text)"/></svg>Like</span>
      <span class="action-button action-button--comment"><svg width="14" height="12" viewBox="0 0 14 12"><ellipse cx="7" cy="5.5" rx="6.5" ry="5" fill="var(--button-text)"/></svg>Comment</span>
      <span class="action-button action-button--more"><svg width="22" height="6" viewBox="0 0 22 6"><circle cx="3" cy="3" r="2.6" fill="var(--button-text)"/><circle cx="11" cy="3" r="2.6" fill="var(--button-text)"/><circle cx="19" cy="3" r="2.6" fill="var(--button-text)"/></svg></span>
    </div>

    <nav class="app-nav">
      <span class="nav-item"><svg width="22" height="20" viewBox="0 0 22 20"><path d="M11 1 L21 10 H18 V19 H13 V13 H9 V19 H4 V10 H1 Z" fill="#fff"/></svg></span>
      <span class="nav-item"><svg width="20" height="20" viewBox="0 0 20 20"><circle cx="8" cy="8" r="6" fill="none" stroke="#bbb" stroke-width="2.5"/><path d="M12.5 12.5 L18 18" stroke="#bbb" stroke-width="3"/></svg></span>
      <span class="nav-item nav-item--active"><svg width="22" height="22" viewBox="0 0 22 22"><rect x="1" y="1" width="20" height="20" rx="2" fill="#fff"/></svg></span>
      <span class="nav-item"><svg width="22" height="20" viewBox="0 0 22 20"><ellipse cx="11" cy="9" rx="10" ry="8" fill="#bbb"/></svg></span>
      <span class="nav-item"><svg width="20" height="20" viewBox="0 0 20 20"><circle cx="10" cy="6" r="5" fill="#bbb"/><path d="M1 20 Q1 11 10 11 Q19 11 19 20 Z" fill="#bbb"/></svg></span>
    </nav>
  </section>

  <!-- Where's my gym buddy? frame -->
  <section class="selfie-frame selfie-frame--buddy">
    <div class="side-band side-band--left"></div>
    <div class="side-band side-band--right"></div>

    <header class="app-header">
      <svg class="status-dots" width="26" height="6" viewBox="0 0 26 6"><circle cx="3" cy="3" r="2.5" fill="#fff"/><circle cx="9" cy="3" r="2.5" fill="#fff"/><circle cx="15" cy="3" r="2.5" fill="#fff"/><circle cx="21" cy="3" r="2.2" fill="none" stroke="#fff"/></svg>
      <svg class="battery" width="22" height="9" viewBox="0 0 22 9"><rect x="0.5" y="0.5" width="19" height="8" fill="none" stroke="#fff"/><rect x="2" y="2" width="12" height="5" fill="var(--battery-green)"/><rect x="20" y="3" width="2" height="3" fill="#fff"/></svg>
      <h1 class="app-title">Where's my gym buddy?</h1>
      <svg class="inbox-icon" width="20" height="18" viewBox="0 0 20 18"><path d="M2 7 L5 1 H15 L18 7 V16 H2 Z M2 7 H7 V10 H13 V7 H18" fill="none" stroke="#fff" stroke-width="2" stroke-linejoin="round"/></svg>
    </header>

    <div class="post-avatar"></div>
    <svg class="post-time" width="10" height="10" viewBox="0 0 10 10"><circle cx="5" cy="5" r="4.5" fill="var(--meta-grey)"/><path d="M5 2.5 V5 H7" stroke="#fff" stroke-width="1" fill="none"/></svg>

    <div class="selfie-photo" role="img" aria-label="Open selfie window, soft blurred blue-green backdrop"></div>

    <div class="post-caption">
      <p><svg class="caption-icon" width="9" height="8" viewBox="0 0 9 8"><path d="M4.5 7.5 L0.8 3.8 A2 2 0 0 1 4.5 1.5 A2 2 0 0 1 8.2 3.8 Z" fill="#bbb"/></svg>Tag a friend who should be at the gym,</p>
      <p><svg class="caption-icon" width="9" height="8" viewBox="0 0 9 8"><ellipse cx="4.5" cy="3.7" rx="4.2" ry="3.3" fill="#bbb"/></svg>T.C.tag your posts to @brightloopsydney</p>
      <p>to win points for the competition</p>
    </div>

    <div class="post-actions">
      <span class="action-button action-button--like"><svg width="13" height="12" viewBox="0 0 9 8"><path d="M4.5 7.5 L0.8 3.8 A2 2 0 0 1 4.5 1.5 A2 2 0 0 1 8.2 3.8 Z" fill="var(--button-text)"/></svg>Like</span>
      <span class="action-button action-button--comment"><svg width="14" height="12" viewBox="0 0 14 12"><ellipse cx="7" cy="5.5" rx="6.5" ry="5" fill="var(--button-text)"/></svg>Comment</span>
      <span class="action-button action-button--more"><svg width="22" height="6" viewBox="0 0 22 6"><circle cx="3" cy="3" r="2.6" fill="var(--button-text)"/><circle cx="11" cy="3" r="2.6" fill="var(--button-text)"/><circle cx="19" cy="3" r="2.6" fill="var(--button-text)"/></svg></span>
    </div>

    <nav class="app-nav">
      <span class="nav-item"><svg width="22" height="20" viewBox="0 0 22 20"><path d="M11 1 L21 10 H18 V19 H13 V13 H9 V19 H4 V10 H1 Z" fill="#fff"/></svg></span>
      <span class="nav-item"><svg width="20" height="20" viewBox="0 0 20 20"><circle cx="8" cy="8" r="6" fill="none" stroke="#bbb" stroke-width="2.5"/><path d="M12.5 12.5 L18 18" stroke="#bbb" stroke-width="3"/></svg></span>
      <span class="nav-item nav-item--active"><svg width="22" height="22" viewBox="0 0 22 22"><rect x="1" y="1" width="20" height="20" rx="2" fill="#fff"/></svg></span>
      <span class="nav-item"><svg width="22" height="20" viewBox="0 0 22 20"><ellipse cx="11" cy="9" rx="10" ry="8" fill="#bbb"/></svg></span>
      <span class="nav-item"><svg width="20" height="20" viewBox="0 0 20 20"><circle cx="10" cy="6" r="5" fill="#bbb"/><path d="M1 20 Q1 11 10 11 Q19 11 19 20 Z" fill="#bbb"/></svg></span>
    </nav>
  </section>

</main>
</body>
</html>
```